Business Card Design

Freelance writer, coach, teacher and researcher specialising in improving mathematics teaching and learning in primary schools. I write books and articles for teachers, speak extensively at conferences in UK and aboard. Would like something with a cube in the design. Clean, modern - logo suitable for use on a website. Should NOT look 'childish' (no comic sans or chalkboard type fonts)

Full details to go on card:

Professor Dan Theroll
Unlocking Early Numeracy

info@dantheroll.net
#dantheroll26
www.dantheroll.net
+44 7812 660 394

Industry/Entity Type

Teacher

Contact Information for Business Card

Professor Dan Theroll
Unlocking Early Numbers

```html
<!DOCTYPE html>
<html lang="en">
<head>
<meta charset="utf-8">
<title>Unlocking Early Numeracy – Business Card</title>
<link rel="stylesheet" href="https://fonts.googleapis.com/css2?family=Nunito:wght@300;700;800&display=swap">
<style>
  :root {
    --backdrop: #eef1f1;
    --card: #ffffff;
    --teal: #1f8a80;
    --teal-mark: #3fb8b3;
    --ink: #333333;
    --ink-soft: #555555;
  }
  html, body {
    margin: 0;
    padding: 0;
    width: 1200px;
    height: 1000px;
    overflow: hidden;
    background: var(--backdrop);
    font-family: "Nunito", Arial, sans-serif;
  }
  .business-card {
    position: absolute;
    left: 150px;
    top: 220px;
    width: 900px;
    height: 560px;
    background: var(--card);
    box-shadow: 0 2px 10px rgba(0, 0, 0, 0.08);
  }
  .brand-square {
    position: absolute;
    left: 90px;
    top: 90px;
    width: 190px;
    height: 190px;
  }
  .card-details {
    position: absolute;
    left: 400px;
    top: 110px;
    right: 40px;
  }
  .brand-title {
    margin: 0;
    font-size: 54px;
    line-height: 0.95;
    font-weight: 800;
    color: var(--teal);
  }
  .person-name {
    margin: 34px 0 0;
    font-size: 34px;
    font-weight: 700;
    color: var(--ink);
  }
  .contact-list {
    list-style: none;
    margin: 24px 0 0;
    padding: 0;
    font-size: 26px;
    line-height: 1.3;
    font-weight: 300;
    color: var(--ink-soft);
  }
</style>
</head>
<body>
  <main class="business-card">
    <svg class="brand-square" viewBox="0 0 190 190" aria-hidden="true">
      <rect x="0" y="0" width="190" height="190" fill="var(--teal-mark)"/>
    </svg>
    <section class="card-details">
      <h1 class="brand-title">Unlocking<br>Early<br>Numeracy</h1>
      <p class="person-name">Professor Dan Theroll</p>
      <ul class="contact-list">
        <li>info@dantheroll.net</li>
        <li>#dantheroll26</li>
        <li>www.dantheroll.net</li>
        <li>+44 7812 660 394</li>
      </ul>
    </section>
  </main>
</body>
</html>
```